Life Insurance For Real Life

this is a statement I came up with - I am selling insurance based on the fact that I have gone through exactly what insurance can do for everyone: <br/>It’s not “just insurance” it’s a life jacket when you can’t stop the boat from sinking. Think about it…. Will you be safe? Will your family be safe if tragedy takes you away? Who will pay all the expenses if you or your spouse are not here anymore? Believe me, I know. Let me help you take care of the ones you love. <br/>Call me: 555-218-6093, Mae Lynn Borsky <br/>“REAL LIFE EXPERIENCE FOR REAL LIFE”<br/>

Target Market(s)

New Jersey (USA) seniors ages 65-80.

Industry/Entity Type

Insurance

Colors

Designer to choose colors to be used in the design.

Requirements
Must have
• Good photo of family people who look like they are concerned with family matters - I do not want my name or company name on the first page. I also want a button they can press and get to a second page where they enter contact info and include a email us now type button with a direct email from their device to me.
Nice to have
• maybe an interracial couple with 2-3 kids and a mid-life aged couple - 40-something or so - people who look like they want to make sure their family is safe and taken care of. I am looking to play on emotions to get people to think.
Should not have
• should not have my name or company name

```html
<!DOCTYPE html>
<html lang="en">
<head>
<meta charset="utf-8">
<title>Life Insurance For Real Life</title>
<link href="https://fonts.googleapis.com/css2?family=Poppins:wght@400;500;600&display=swap" rel="stylesheet">
<style>
  :root{
    --backdrop:#212b3d;
    --paper:#ffffff;
    --slate:#3f5676;
    --slate-dark:#2f4462;
    --green:#1fb51a;
    --green-bright:#2ecf24;
    --ink:#111418;
    --red:#ee1111;
    --olive:#7a8a1e;
  }
  *{box-sizing:border-box;margin:0;padding:0}
  html,body{width:1200px;height:1200px;overflow:hidden;background:var(--backdrop)}
  body{font-family:"Poppins",sans-serif;position:relative}
  .banner{position:absolute;left:41px;top:291px;width:1118px;height:642px;background:var(--paper);overflow:hidden}
  .family-photo{position:absolute;right:0;top:0;width:640px;height:642px;
    background:
      radial-gradient(ellipse at 60% 35%, #e9b99a 0%, rgba(233,185,154,0) 45%),
      radial-gradient(ellipse at 75% 75%, #8fb7d8 0%, rgba(143,183,216,0) 40%),
      radial-gradient(ellipse at 90% 20%, #b49a55 0%, rgba(180,154,85,0) 45%),
      linear-gradient(135deg,#d8c7a0 0%,#c7a98a 40%,#7e9a5c 75%,#a9b9c9 100%);
    -webkit-mask-image:linear-gradient(to right,transparent 0%,#000 30%);
    mask-image:linear-gradient(to right,transparent 0%,#000 30%)}
  .copy{position:absolute;left:47px;top:33px;width:600px}
  .intro{color:var(--slate);font-weight:400;line-height:1.45}
  .intro .lead{font-size:27px;line-height:1.2}
  .intro .sub{font-size:22px}
  .hook{color:var(--green);font-weight:600;font-size:24px;line-height:1.42;margin-top:12px}
  .question{color:var(--ink);font-weight:600;font-size:32px;line-height:1.3;margin-top:6px}
  .worry{color:var(--green);font-weight:400;font-size:24px;line-height:1.45;margin-top:10px}
  .assure{color:var(--slate);font-weight:600;font-size:24px;line-height:1.5;margin-top:10px}
  .assure .big{font-size:27px}
  .assure .love{color:var(--red)}
  .btn{position:absolute;top:515px;height:48px;border-radius:24px;color:#fff;display:flex;align-items:center;justify-content:center;text-decoration:none}
  .btn-email{left:47px;width:270px;background:linear-gradient(#5b7293,var(--slate-dark));font-size:28px;font-weight:500}
  .btn-call{left:331px;width:370px;background:linear-gradient(var(--green-bright),var(--green));font-size:27px;font-weight:600}
  .tagline{position:absolute;left:0;right:0;top:580px;height:44px;display:flex;align-items:center}
  .tagline .rule{height:3px;background:var(--slate)}
  .tagline .rule.left{width:277px}
  .tagline .rule.right{flex:1}
  .tagline .text{font-size:32px;color:var(--slate);padding:0 12px;white-space:nowrap}
  .tagline .accent{color:var(--olive)}
</style>
</head>
<body>
  <section class="banner">
    <div class="family-photo" role="img" aria-label="Photo of a smiling family of four playing together outdoors in a sunny park"></div>
    <div class="copy">
      <p class="intro"><span class="lead">I am selling insurance based on the fact</span><br><span class="sub">that I have gone through exactly<br>what insurance can do for everyone:</span></p>
      <p class="hook">It’s not “just insurance” it’s a life jacket<br>when you can’t stop the boat from sinking.</p>
      <p class="question">Think about it…. Will you be safe?<br>Will your family be safe if tragedy<br>takes you away?</p>
      <p class="worry">Who will pay all the expenses if you<br>or your spouse are not here anymore?</p>
      <p class="assure"><span class="big">Believe me, I know.</span> Let me help you<br>take care of the ones <span class="love">you love.</span></p>
    </div>
    <a class="btn btn-email" href="#contact">Email us now</a>
    <a class="btn btn-call" href="tel:5552186093">CALL ME : 555-218-6093</a>
    <div class="tagline">
      <span class="rule left"></span>
      <span class="text">Real life <span class="accent">experience for real</span> life</span>
      <span class="rule right"></span>
    </div>
  </section>
</body>
</html>
```